high-impact, conversion-focused website redesign for the government sector

Objective: To design and develop a high-impact, conversion-focused digital platform that solidifies Harrowfield Bright Associates (HBA) as the leading communications and strategy firm for government, defense, and industrial clients. The site must project authority, innovation, and sophisticated precision. See the creative breif for more information

Target Market(s)

Government contractors

Industry/Entity Type

Government, defense, industrials

Coding

Coded - Design and coding required

Number of Pages Required

5+ page

Font styles to use
Other font styles liked:
• See the current website

Requirements
Must have
• See design brief
Nice to have
• See design brief
Should not have
• See design brief

```html
<!DOCTYPE html>
<html lang="en">
<head>
<meta charset="utf-8">
<title>Harrowfield Bright Associates — Accelerate Your Mission</title>
<link href="https://fonts.googleapis.com/css2?family=Michroma&family=Poppins:wght@400;500;600&display=swap" rel="stylesheet">
<style>
:root{
  --navy:#0a1628;--navy-2:#0d2038;--deep:#060d18;--green:#7cc242;--green-d:#5f9f2a;
  --blue:#1e8fe3;--orange:#f7941d;--orange-d:#f15a22;--teal:#113b4e;--paper:#f3f5f8;
  --ink:#1c2a3d;--muted:#5d6878;--line:#dfe4ea;--white:#fff;
  --head:"Michroma",sans-serif;--body:"Poppins",sans-serif;
}
*{box-sizing:border-box;margin:0;padding:0}
html,body{width:1200px;height:4796px;overflow:hidden}
body{font-family:var(--body);color:var(--ink);background:var(--navy);position:relative}
section,header,footer{position:absolute;left:0;width:1200px}
.abs{position:absolute}
.h{font-family:var(--head);text-transform:uppercase;letter-spacing:.5px;line-height:1.4;font-weight:400}
.g{color:var(--green)}
.center{text-align:center;left:0;width:1200px}
.btn{position:absolute;display:flex;align-items:center;justify-content:space-between;height:28px;padding:0 8px 0 14px;background:var(--white);color:var(--ink);font-size:12px;font-weight:500;border:1px solid var(--ink)}
.btn svg{width:30px;height:20px}
.btn.dark{background:transparent;color:var(--ink)}
/* hero */
.hero{top:0;height:1310px;background:linear-gradient(180deg,#0b1322 0%,#0a1628 60%,#0b1b33 100%);color:var(--white);overflow:hidden}
.space{position:absolute;inset:0;background:
 radial-gradient(ellipse 520px 420px at 980px 520px,#1d3b66 0%,rgba(20,40,70,.5) 45%,transparent 70%),
 radial-gradient(ellipse 300px 260px at 250px 300px,rgba(80,70,60,.35),transparent 70%),
 radial-gradient(ellipse 700px 300px at 600px 1100px,rgba(20,50,90,.45),transparent 70%)}
.nav a{position:absolute;top:18px;color:var(--white);text-decoration:none;font-size:13px}
.brand{position:absolute;display:flex;align-items:center;gap:8px;color:var(--white);font-family:var(--body);font-weight:500}
.brand .sq{width:14px;height:14px;background:var(--blue)}
.brand .txt{line-height:1.1;font-size:13px;letter-spacing:1px;text-align:center}
.brand .txt small{display:block;font-size:8px;letter-spacing:3px}
.arrow-sq{position:absolute;width:26px;height:26px;border:1px solid #8a96a8;display:flex;align-items:center;justify-content:center}
.stat{position:absolute;width:320px;text-align:center;top:856px}
.stat b{display:block;font-family:var(--head);font-weight:400;font-size:26px}
.stat p{font-size:11.5px;margin-top:14px;line-height:1.45;color:#d4dbe6}
.stat i{position:absolute;left:130px;top:93px;width:60px;height:3px;background:var(--green)}
.quote{position:absolute;top:1089px;height:158px;border:1px solid #7b8798;background:rgba(6,13,24,.6);padding:30px 40px;text-align:center}
.quote .who{font-size:13.5px;font-weight:500}
.quote p{font-size:9.5px;line-height:1.75;color:#c8d0dc;margin-top:20px}
.quote .qm{position:absolute;top:-14px;font-family:var(--head);font-size:52px;color:#5e6a7b;line-height:1}
.quote.faded{opacity:.35;border-color:#3b4657}
/* services */
.services{top:1310px;height:708px;background:var(--paper)}
.card{position:absolute;width:231px;height:231px;background:var(--white);text-align:center;padding-top:12px;border:1px solid transparent}
.card .num{font-size:12px;color:var(--muted)}
.card svg.hex{display:block;margin:8px auto 0;width:48px;height:52px}
.card h3{font-size:14px;font-weight:500;margin-top:14px}
.card p{font-size:9.5px;line-height:1.7;color:var(--muted);width:185px;margin:22px auto 0}
.card .go{position:absolute;right:0;bottom:0;width:26px;height:26px;background:#c9d0d8;display:flex;align-items:center;justify-content:center}
.card.on{border-color:var(--green)}
.card.on .num,.card.on h3{color:var(--green-d)}
.card.on .go{background:var(--green)}
/* advisors */
.advisors{top:2018px;height:332px;background:linear-gradient(90deg,#0b1a30 0%,#0e2746 60%,#0a1a30 100%);color:var(--white);overflow:hidden}
.advisors p{font-size:9.5px;line-height:1.7;color:#c8d0dc}
.art{position:absolute;left:125px;top:0;width:345px;height:275px;background:linear-gradient(120deg,#f7941d 0%,#1e8fe3 45%,#5f9f2a 100%);opacity:.85}
/* edge */
.edge{top:2350px;height:456px;background:var(--white)}
.edge p{font-size:11.5px;line-height:1.8;color:var(--ink)}
/* insights */
.insights{top:2806px;height:654px;background:linear-gradient(180deg,#08111e,#0b1a2e);color:var(--white)}
.post{position:absolute;overflow:hidden}
.post .tag{position:absolute;left:0;top:0;background:var(--green);color:var(--white);font-size:11px;padding:3px 10px}
.post h4{font-size:14px;font-weight:500;line-height:1.45}
.post .wn{position:absolute;background:var(--white);color:var(--ink);font-size:12px;padding:6px 14px}
/* expect */
.expect{top:3460px;height:740px;background:var(--white)}
.expect p{font-size:11px;line-height:1.85;color:var(--ink)}
.expect b{font-weight:600}
.wheel{position:absolute;left:147px;top:105px;width:400px;height:400px;border-radius:50%;background:radial-gradient(circle,#0b0f16 0%,#0b0f16 25%,#a9d67c 27%,#7cc242 60%,#1e8fe3 85%,#f7941d 100%)}
/* cta + footer */
.lower{top:4199px;height:597px;background:var(--navy)}
.cta{position:absolute;left:125px;top:4115px;width:951px;height:289px;background:linear-gradient(120deg,#0a1424,#10233d 60%,#0a1629);color:var(--white);text-align:center}
.ghost{top:4410px;font-family:var(--head);font-size:66px;color:rgba(255,255,255,.06);white-space:nowrap;text-align:center;letter-spacing:2px}
.fcol h5{font-size:12px;font-weight:500;color:var(--white);padding-bottom:8px;border-bottom:2px solid var(--green);display:inline-block}
.fcol ul{list-style:none;margin-top:16px}
.fcol li{font-size:10px;color:#c8d0dc;line-height:1.75}
.vline{position:absolute;top:4506px;width:1px;height:224px;background:#2a3b55}
</style>
</head>
<body>

<header class="hero">
  <div class="space" role="img" aria-label="Night-side Earth seen from orbit with a starfield"></div>
  <nav class="nav">
    <a style="left:251px">Advisory Services</a>
    <a style="left:409px">About Us</a>
    <a style="left:735px">Blog</a>
    <a style="left:820px">Contact Us</a>
  </nav>
  <div class="brand" style="left:505px;top:28px"><span class="sq"></span><span class="txt">HARROWFIELD BRIGHT<small>ASSOCIATES</small></span></div>

  <h1 class="h abs center" style="top:222px;font-size:52px;color:var(--green)">Accelerate</h1>
  <h1 class="h abs center" style="top:280px;font-size:74px">Your Mission</h1>
  <p class="abs" style="left:287px;top:391px;width:626px;text-align:center;font-size:12.5px;line-height:1.85">Harrowfield Bright Associates exists for one reason to help connect the federal ecosystem with the technologies that matter most to America and her allies. We help build the communications, government affairs and marketing strategies and systems your organization needs to grow and protect market share –helping our clients meet their mission objectives.</p>
  <a class="btn" style="left:486px;top:506px;width:227px;border:0">View Our Advisory Services
    <svg viewBox="0 0 30 20"><path d="M4 2l9 8-9 8h7l9-8-9-8z" fill="var(--green)"/><path d="M13 2l9 8-9 8h6l9-8-9-8z" fill="var(--blue)"/></svg></a>
  <div class="arrow-sq" style="left:125px;top:413px"><svg width="10" height="10" viewBox="0 0 10 10"><path d="M7 1L3 5l4 4" stroke="#fff" fill="none" stroke-width="1.5"/></svg></div>
  <div class="arrow-sq" style="left:1048px;top:413px"><svg width="10" height="10" viewBox="0 0 10 10"><path d="M3 1l4 4-4 4" stroke="#fff" fill="none" stroke-width="1.5"/></svg></div>
  <div class="abs" style="left:599px;top:568px;width:2px;height:93px;background:var(--green)"></div>

  <h2 class="h abs center" style="top:692px;font-size:24px;line-height:1.5">Proven Results That Drive<br>Real <span class="g">Growth</span></h2>
  <p class="abs center" style="top:768px;font-size:11.5px;line-height:1.7;color:#c8d0dc">We've helped brands strengthen their digital presence, expand their network, and accelerate opportunities<br>across the defense, space, and government sectors. In just one year, our clients have achieved :</p>
  <div class="stat" style="left:114px"><b>+72%</b><p>Increase in database contacts via<br>CRM + <span style="color:#fff">targeted</span> campaigns</p><i></i></div>
  <div class="stat" style="left:440px"><b>100+</b><p>Introductions to <span style="color:#fff">tech-scouting contracts</span><br>across DoD and aerospace/defense</p><i></i></div>
  <div class="stat" style="left:765px"><b>570%</b><p>stock growth / <span style="color:#fff">$50M AUD</span> in new<br>investment for a rapidly scaling client</p><i></i></div>
  <div class="abs" style="left:177px;top:951px;width:846px;height:1px;background:#3c4a60"></div>

  <h2 class="h abs center" style="top:1024px;font-size:24px">Our <span class="g">Client</span> Quotes</h2>
  <div class="quote faded" style="left:-40px;width:306px;text-align:left"><span class="qm" style="right:30px">“</span><div class="who">ment Lead</div><p>An innovative approach and strategic insight propelled our team forward, building stakeholder trust across the sector.</p></div>
  <div class="quote" style="left:285px;width:629px"><span class="qm" style="left:40px">“</span><span class="qm" style="right:40px">”</span>
    <div class="who">Daniel Marrow, President and Managing Director</div>
    <p>Partnering with Harrowfield Bright Associates accelerated the growth of our company. Their strategic insight, deep federal expertise, and hands-on support transformed our U.S. expansion. In less than six months, they built our presence in the United States from the ground up, helping us secure contacts, advocates, and visibility at the highest levels. Working with Harrowfield Bright Associates has been a true game-changer for our company.”</p></div>
  <div class="quote faded" style="left:940px;width:300px;text-align:right"><span class="qm" style="left:20px">“</span><div class="who">Laura Pennick, V</div><p>Working with Harrowfield Bright Associates for our mission at Summit Works, the result was focused outreach, new partners and lasting value for our innovation community.</p></div>
</header>

<section class="services">
  <h2 class="h abs center" style="top:60px;font-size:24px">Our Advisory <span class="g">Services</span></h2>
  <p class="abs center" style="top:105px;font-size:12px;color:var(--muted)">Strategic support to strengthen your position across the federal ecosystem.</p>

  <div class="card" style="left:125px;top:150px"><div class="num">01</div><svg class="hex" viewBox="0 0 48 52"><polygon points="24,1 47,14 47,38 24,51 1,38 1,14" fill="var(--teal)"/><rect x="15" y="20" width="18" height="13" fill="none" stroke="#fff" stroke-width="1.6"/></svg><h3>Corporate Communications</h3><p>Clear, compelling messaging that defines your mission, sharpens your narrative, and aligns your organization internally and externally.</p><span class="go"><svg width="10" height="10" viewBox="0 0 10 10"><path d="M2 8l6-6M3 2h5v5" stroke="#1c2a3d" fill="none" stroke-width="1.4"/></svg></span></div>
  <div class="card on" style="left:365px;top:150px"><div class="num">02</div><svg class="hex" viewBox="0 0 48 52"><polygon points="24,1 47,14 47,38 24,51 1,38 1,14" fill="var(--green)"/><path d="M15 22h5l9-5v18l-9-5h-5z" fill="none" stroke="#fff" stroke-width="1.6"/></svg><h3>Public Relations</h3><p>Media engagement, press strategy, and thought-leadership campaigns that elevate your voice in the defense, technology, and government markets.</p><span class="go"><svg width="10" height="10" viewBox="0 0 10 10"><path d="M2 8l6-6M3 2h5v5" stroke="#fff" fill="none" stroke-width="1.4"/></svg></span></div>
  <div class="card" style="left:605px;top:150px"><div class="num">03</div><svg class="hex" viewBox="0 0 48 52"><polygon points="24,1 47,14 47,38 24,51 1,38 1,14" fill="var(--teal)"/><circle cx="18" cy="30" r="4" fill="none" stroke="#fff" stroke-width="1.6"/><circle cx="30" cy="21" r="4" fill="none" stroke="#fff" stroke-width="1.6"/><path d="M21 28l6-5" stroke="#fff" stroke-width="1.6"/></svg><h3>Government Affairs</h3><p>Strategic guidance and relationship-building to help you navigate policy environments, engage federal stakeholders, and advance mission-aligned objectives.</p><span class="go"><svg width="10" height="10" viewBox="0 0 10 10"><path d="M2 8l6-6M3 2h5v5" stroke="#1c2a3d" fill="none" stroke-width="1.4"/></svg></span></div>
  <div class="card" style="left:845px;top:150px"><div class="num">04</div><svg class="hex" viewBox="0 0 48 52"><polygon points="24,1 47,14 47,38 24,51 1,38 1,14" fill="var(--teal)"/><circle cx="24" cy="26" r="6" fill="none" stroke="#fff" stroke-width="1.6"/><path d="M24 14v6M24 32v6M12 26h6M30 26h6" stroke="#fff" stroke-width="1.6"/></svg><h3>Crisis Communications</h3><p>Rapid, precise, and disciplined communication support to protect your reputation and manage high-risk moments with confidence.</p><span class="go"><svg width="10" height="10" viewBox="0 0 10 10"><path d="M2 8l6-6M3 2h5v5" stroke="#1c2a3d" fill="none" stroke-width="1.4"/></svg></span></div>

  <div class="card" style="left:125px;top:412px"><div class="num">05</div><svg class="hex" viewBox="0 0 48 52"><polygon points="24,1 47,14 47,38 24,51 1,38 1,14" fill="var(--teal)"/><rect x="18" y="16" width="12" height="20" rx="2" fill="none" stroke="#fff" stroke-width="1.6"/></svg><h3>Digital Marketing</h3><p>Targeted campaigns, CRM systems, analytics, and online strategy to strengthen your digital footprint and accelerate growth opportunities.</p><span class="go"><svg width="10" height="10" viewBox="0 0 10 10"><path d="M2 8l6-6M3 2h5v5" stroke="#1c2a3d" fill="none" stroke-width="1.4"/></svg></span></div>
  <div class="card" style="left:365px;top:412px"><div class="num">06</div><svg class="hex" viewBox="0 0 48 52"><polygon points="24,1 47,14 47,38 24,51 1,38 1,14" fill="var(--teal)"/><rect x="15" y="17" width="7" height="7" fill="none" stroke="#fff" stroke-width="1.5"/><rect x="26" y="28" width="7" height="7" fill="none" stroke="#fff" stroke-width="1.5"/><path d="M22 21h7v7" stroke="#fff" fill="none" stroke-width="1.5"/></svg><h3>Strategic Connections</h3><p>Direct access to a powerful network across DoD, federal agencies, industry leaders, investors, and innovators to open doors and expand opportunities.</p><span class="go"><svg width="10" height="10" viewBox="0 0 10 10"><path d="M2 8l6-6M3 2h5v5" stroke="#1c2a3d" fill="none" stroke-width="1.4"/></svg></span></div>
  <div class="card" style="left:605px;top:412px"><div class="num">07</div><svg class="hex" viewBox="0 0 48 52"><polygon points="24,1 47,14 47,38 24,51 1,38 1,14" fill="var(--teal)"/><path d="M15 34l7-8 5 4 7-10" stroke="#fff" fill="none" stroke-width="1.6"/></svg><h3>Investor Relations</h3><p>Messaging, positioning, and communications that support fundraising, valuation increases, market transitions, and investor confidence.</p><span class="go"><svg width="10" height="10" viewBox="0 0 10 10"><path d="M2 8l6-6M3 2h5v5" stroke="#1c2a3d" fill="none" stroke-width="1.4"/></svg></span></div>
  <div class="card" style="left:845px;top:412px"><div class="num">08</div><svg class="hex" viewBox="0 0 48 52"><polygon points="24,1 47,14 47,38 24,51 1,38 1,14" fill="var(--teal)"/><rect x="15" y="18" width="18" height="16" fill="none" stroke="#fff" stroke-width="1.6"/><path d="M15 23h18M19 15v5M29 15v5" stroke="#fff" stroke-width="1.6"/></svg><h3>Event Management</h3><p>End-to-end planning, speaker acquisition, logistics, and promotional strategy for high-impact events in the federal and defense innovation ecosystem.</p><span class="go"><svg width="10" height="10" viewBox="0 0 10 10"><path d="M2 8l6-6M3 2h5v5" stroke="#1c2a3d" fill="none" stroke-width="1.4"/></svg></span></div>
</section>

<section class="advisors">
  <div class="art" role="img" aria-label="Geometric composition of coloured triangles and a diamond framing an astronaut in a spacecraft"></div>
  <h2 class="h abs" style="left:566px;top:50px;font-size:24px;line-height:1.5">Strategic Advisors for High-<br>Stakes Environments</h2>
  <p class="abs" style="left:566px;top:138px;width:520px">Harrowfield Bright Associates is a mission-driven advisory firm supporting innovators across defense, aerospace, national security, and federal technology. With a team of former military leaders, federal communicators, and industry strategists, we help organizations build the communications, government affairs, and marketing systems needed to grow in complex federal environments. Our deep sector insight and powerful network drive measurable outcomes that strengthen positioning, accelerate opportunity, and support mission success.</p>
  <a class="btn" style="left:566px;top:243px;width:170px;border:0">Learn About Us
    <svg viewBox="0 0 30 20"><path d="M4 2l9 8-9 8h7l9-8-9-8z" fill="var(--green)"/><path d="M13 2l9 8-9 8h6l9-8-9-8z" fill="var(--blue)"/></svg></a>
</section>

<section class="edge">
  <h2 class="h abs" style="left:125px;top:64px;font-size:24px">Our <span class="g">Edge</span></h2>
  <p class="abs" style="left:125px;top:103px;width:300px;color:var(--muted)">A strategic edge shaped by decades inside the federal ecosystem.</p>
  <p class="abs" style="left:125px;top:168px;width:400px">We combine deep federal sector insight, technical understanding, and a powerful network across government, industry, investors, and media. Our proven approach drives results — from major contract wins and successful M&amp;A to increased valuation, strategic investment, and political support.<br>Our strategies begin with your mission and business goals, ensuring every message, relationship, and action advances growth and impact.</p>
  <a class="btn dark" style="left:125px;top:362px;width:180px">Explore Our EDGE
    <svg viewBox="0 0 30 20"><path d="M4 2l9 8-9 8h7l9-8-9-8z" fill="var(--green)"/><path d="M13 2l9 8-9 8h6l9-8-9-8z" fill="var(--blue)"/></svg></a>
  <div class="abs" style="left:542px;top:89px;width:520px;height:306px;background:var(--blue)"></div>
  <div class="abs" role="img" aria-label="Operations control room with monitors showing a world map" style="left:553px;top:65px;width:523px;height:318px;background:linear-gradient(160deg,#3d5a62 0%,#24383f 45%,#141e24 100%);border:3px solid #1a2a33"></div>
  <div class="abs" style="left:1046px;top:65px;width:30px;height:30px;background:var(--orange-d)"></div>
</section>

<section class="insights">
  <h2 class="h abs center" style="top:55px;font-size:24px;line-height:1.55">Insights From the Federal<br><span class="g">Innovation</span> Frontline</h2>
  <p class="abs center" style="top:140px;font-size:12px;line-height:1.7;color:#c8d0dc">Our blog covers emerging technologies, policy shifts, industry trends, and practical<br>strategies to help organizations thrive in the federal ecosystem.</p>

  <div class="post" role="img" aria-label="Laptop showing a technology dashboard" style="left:125px;top:205px;width:519px;height:322px;background:linear-gradient(180deg,#31465a 0%,#1d3047 55%,#1a3a6c 100%)">
    <span class="tag">Defense Tech</span>
    <h4 class="abs" style="left:24px;top:200px;width:330px">How Dual-Use Technology Is Transforming the Defense Innovation Pipeline</h4>
    <p class="abs" style="left:24px;top:250px;width:330px;font-size:9.5px;line-height:1.55;color:#cfd7e2">Emerging dual-use technologies are reshaping how the DoD evaluates, procures, and deploys new capabilities. This article breaks down the trends shaping 2025—and what innovators must understand to stay ahead of shifting defense priorities.</p>
    <span class="wn" style="left:392px;top:268px">Watch Now</span>
  </div>
  <div class="post" role="img" aria-label="Business people standing before a city skyline at dusk" style="left:655px;top:205px;width:421px;height:155px;background:linear-gradient(180deg,#4a6f9e 0%,#27466e 50%,#14243b 100%)">
    <span class="tag">Policy &amp; Government Affairs</span>
    <h4 class="abs" style="left:12px;top:98px;width:290px;font-size:13px">Navigating Federal Policy Shifts: What Contractors Need to Know Now</h4>
    <span class="wn" style="left:312px;top:108px">Watch Now</span>
  </div>
  <div class="post" role="img" aria-label="Hand using a tablet with holographic interface" style="left:655px;top:372px;width:421px;height:155px;background:linear-gradient(180deg,#5c7282 0%,#34495a 55%,#16222f 100%)">
    <span class="tag">GovComms &amp; Strategy</span>
    <h4 class="abs" style="left:12px;top:98px;width:290px;font-size:13px">Building a Federal Communications Strategy That Cuts Through the Noise</h4>
    <span class="wn" style="left:312px;top:108px">Watch Now</span>
  </div>
  <a class="btn" style="left:510px;top:564px;width:180px;border:0">View All Blogs
    <svg viewBox="0 0 30 20"><path d="M4 2l9 8-9 8h7l9-8-9-8z" fill="var(--green)"/><path d="M13 2l9 8-9 8h6l9-8-9-8z" fill="var(--blue)"/></svg></a>
</section>

<section class="expect">
  <div class="wheel" role="img" aria-label="Circular brand growth diagram with service segments around a central brand core"></div>
  <h2 class="h abs" style="left:600px;top:66px;font-size:24px;line-height:1.5">What to Expect When<br><span class="g">Partnering</span> With Us</h2>
  <p class="abs" style="left:600px;top:137px;width:480px;color:var(--muted)">Our structured approach ensures every engagement begins with insight, aligns with your mission, and delivers results.</p>
  <p class="abs" style="left:600px;top:210px;width:490px">With decades of experience, a <b>results-focused methodology</b>, and cutting-edge marketing and communications tools and technologies, we begin every engagement with a discovery and planning process to ensure we are building a strategy that cuts through the noise to achieve our measurable results. As specialists in government crisis communications, we additionally examine our client's current strategy for risks ensuring we are building on a stable foundation.</p>
  <p class="abs" style="left:600px;top:366px;width:490px">By truly understanding our client's goals, <b>key milestones, potential areas of risk, ideal customer</b> and <b>investor targets, partner profiles,</b> and <b>other key drivers,</b> we create messaging and strategy that goes beyond traditional brand awareness to meet mission objectives. As a full service firm, we work across all the areas in the graphic.</p>
  <p class="abs" style="left:600px;top:484px;width:490px"><b>Our time-tested methodology</b> is based on building and executing a strategy aligned with client mission objectives. With the strategy in place, we execute tactics with precision, efficiency, and the highest quality of customer service.</p>
  <a class="btn dark" style="left:600px;top:576px;width:180px">Get In Touch
    <svg viewBox="0 0 30 20"><path d="M4 2l9 8-9 8h7l9-8-9-8z" fill="var(--green)"/><path d="M13 2l9 8-9 8h6l9-8-9-8z" fill="var(--blue)"/></svg></a>
</section>

<section class="lower"></section>
<div class="cta" role="region" aria-label="Call to action">
  <h2 class="h" style="margin-top:56px;font-size:24px;line-height:1.5">Ready to Accelerate<br>Your Mission?</h2>
  <p style="margin-top:12px;font-size:12px;line-height:1.7;color:#d4dbe6">Let's build the strategy, connections, and communications systems<br>that move your organization forward.</p>
  <a class="btn" style="left:361px;top:196px;width:229px;border:0">Request More Information
    <svg viewBox="0 0 30 20"><path d="M4 2l9 8-9 8h7l9-8-9-8z" fill="var(--green)"/><path d="M13 2l9 8-9 8h6l9-8-9-8z" fill="var(--blue)"/></svg></a>
</div>
<div class="abs ghost center">HARROWFIELD BRIGHT</div>

<footer style="top:4506px;height:290px;color:var(--white)">
  <div class="brand" style="left:125px;top:20px"><span class="sq"></span><span class="txt" style="font-size:16px;text-align:left">HARROWFIELD BRIGHT<small>ASSOCIATES</small></span></div>
  <p class="abs" style="left:125px;top:110px;width:240px;font-size:9.5px;line-height:1.65;color:#c8d0dc">Harrowfield Bright Associates provides strategic communications and government affairs support for organizations operating in the federal ecosystem.</p>
  <div class="abs" style="left:125px;top:176px;width:180px;height:46px;background:#fff;display:flex;gap:6px;padding:5px" role="img" aria-label="Partner and award badges">
    <span style="flex:1;background:#1d3b66"></span><span style="flex:1;background:#3a4658;border-radius:50%"></span><span style="flex:1;background:#0b0f16"></span><span style="flex:1;border:1px solid #0b0f16"></span>
  </div>
</footer>
<div class="vline" style="left:438px"></div>
<div class="vline" style="left:847px"></div>
<div class="abs fcol" style="left:488px;top:4530px"><h5>Quick Links</h5><ul><li style="color:var(--green)">Home</li><li>Advisory Services</li><li>About Us</li><li>Blog</li><li>Contact Us</li></ul></div>
<div class="abs fcol" style="left:665px;top:4530px"><h5>Our Services</h5><ul><li>Corporate Communications</li><li>Public Relations</li><li>Government Affairs (NEW)</li><li>Crisis Communications (NEW)</li><li>Digital Marketing</li><li>Strategic Connections (NEW)</li><li>Investor Relations</li><li>Event Management</li></ul></div>
<div class="abs fcol" style="left:896px;top:4530px"><h5>Contact Us</h5>
  <div style="margin-top:18px;display:flex;gap:8px;font-size:10px;color:var(--green)"><svg width="14" height="14" viewBox="0 0 14 14"><circle cx="7" cy="7" r="7" fill="#fff"/><rect x="3.5" y="4.5" width="7" height="5" fill="none" stroke="#0a1628"/></svg>info@harrowfieldbright.example</div>
  <div style="margin-top:14px;display:flex;gap:8px;font-size:10px;line-height:1.7;color:#c8d0dc"><svg width="14" height="14" viewBox="0 0 14 14"><circle cx="7" cy="7" r="7" fill="#fff"/><circle cx="7" cy="6" r="2" fill="#0a1628"/></svg><span><span style="color:#fff">Summit Works<br>Harrowfield Bright Associates</span><br>418 Lantern Ave<br>Suite 220<br>Austin TX, 78702</span></div>
</div>
<div class="abs" style="left:125px;top:4752px;width:951px;height:1px;background:#2a3b55"></div>
<p class="abs center" style="top:4764px;font-size:10.5px;color:#c8d0dc">© 2025 HARROWFIELD BRIGHT &nbsp;|&nbsp; All Rights Reserved</p>

</body>
</html>
```